Business Card for eCigarette Business

We need a business card design for an e-juice company called Brunoly Tonic Company.

We have 3 lines of signature e-juices called Copper Lantern, Quiet Harbor, and Red Fern.

For this business card, we would like to have the Copper Lantern label on the back of the business card (see attached for PSD). For the front, we want something clean but in the spirit of our logo (see AI file attached).

Content for front:

Logo
312 Linden Ave
Maplecrest, NJ 07412
856-MIST-JOY
856-514-7092
www.brunoly.example

Regards,
Marcus

Target Market(s)

Male, 19 to 50 years old

Industry/Entity Type

Business

Contact Information for Business Card

Content for front:

Logo
312 Linden Ave
Maplecrest, NJ 07412
856-MIST-JOY
856-514-7092
www.brunoly.example

Requirements
Must have
• Note that the Logo should say Brunoly Tonic Co. and Not Cloud Parlor. I've attached the font along with AI file.

```html
<!DOCTYPE html>
<html lang="en">
<head>
<meta charset="utf-8">
<title>Brunoly Tonic Co. — Business Card</title>
<link href="https://fonts.googleapis.com/css2?family=Open+Sans:wght@400;600;700&display=swap" rel="stylesheet">
<style>
  :root {
    --backdrop: #d9d6d3;
    --card-black: #1d1d1f;
    --card-edge: #111113;
    --silver: #6e6e72;
    --silver-soft: #58585c;
    --magenta: #e4177a;
    --violet: #a23aa8;
    --ink-light: #e9e9ea;
    --ink-muted: #bdbdc0;
    --divider: #6a6a6e;
  }
  * { box-sizing: border-box; margin: 0; padding: 0; }
  html, body { width: 1200px; height: 823px; overflow: hidden; }
  body {
    background: var(--backdrop);
    font-family: "Open Sans", Arial, sans-serif;
    position: relative;
  }
  .card {
    position: absolute;
    top: 257px;
    width: 540px;
    height: 309px;
    background: var(--card-black);
    border: 1px solid var(--card-edge);
    border-radius: 4px;
    box-shadow: 0 10px 24px rgba(0,0,0,0.25);
    overflow: hidden;
  }
  .card--back { left: 40px; }
  .card--front { left: 620px; }

  .brand-mark {
    font-weight: 700;
    letter-spacing: 0.5px;
    white-space: nowrap;
  }

  /* Back: Copper Lantern label side */
  .label {
    position: absolute;
    left: 0; right: 0; top: 108px;
    text-align: center;
  }
  .label .brand-mark {
    font-size: 44px;
    line-height: 1.1;
    color: var(--silver);
  }
  .label__flavor {
    margin-top: 10px;
    font-size: 17px;
    font-weight: 600;
    letter-spacing: 4px;
    text-transform: uppercase;
    color: var(--silver-soft);
  }

  /* Front */
  .card--front .brand-mark {
    position: absolute;
    right: 28px; top: 46px;
    font-size: 32px;
    color: var(--violet);
  }

  .person {
    position: absolute;
    left: 20px; top: 140px;
    width: 238px;
    text-align: right;
  }
  .person__name {
    font-size: 27px;
    font-weight: 700;
    color: var(--magenta);
    line-height: 1.15;
    margin-bottom: 4px;
  }
  .person__line {
    font-size: 16px;
    color: var(--ink-muted);
    line-height: 1.45;
  }

  .divider {
    position: absolute;
    left: 274px; top: 140px;
    width: 1px; height: 140px;
    background: var(--divider);
  }

  .contact-list {
    position: absolute;
    left: 290px; top: 140px;
    list-style: none;
  }
  .contact-list li {
    display: flex;
    align-items: center;
    gap: 9px;
    font-size: 16px;
    line-height: 1.6;
    color: var(--ink-light);
    white-space: nowrap;
  }
  .contact-list svg {
    width: 13px; height: 13px;
    fill: var(--magenta);
    flex: none;
  }
</style>
</head>
<body>

  <section class="card card--back" aria-label="Card back, Copper Lantern label">
    <div class="label">
      <div class="brand-mark">Brunoly Tonic Co.</div>
      <p class="label__flavor">Copper Lantern</p>
    </div>
  </section>

  <section class="card card--front" aria-label="Card front">
    <div class="brand-mark">Brunoly Tonic Co.</div>

    <div class="person">
      <p class="person__name">Marcus</p>
      <p class="person__line">Managing Member</p>
      <p class="person__line">312 Linden Ave,</p>
      <p class="person__line">Maplecrest, NJ 07412</p>
    </div>

    <div class="divider"></div>

    <ul class="contact-list">
      <li>
        <svg viewBox="0 0 16 16" aria-hidden="true"><path d="M3.5 1l2.5 3-1.5 1.8c.9 2 2.4 3.5 4.4 4.4L10.7 8.7 13.8 11l-1 3C7 13.6 2.4 9 2 3.2z"/></svg>
        856-MIST-JOY
      </li>
      <li>
        <svg viewBox="0 0 16 16" aria-hidden="true"><path d="M4 1h6l2 2v3H4z M1 7h14v6h-2v2H3v-2H1z M5 11h6v2H5z"/></svg>
        856-514-7092
      </li>
      <li>
        <svg viewBox="0 0 16 16" aria-hidden="true"><path d="M4 0h8a1 1 0 0 1 1 1v14a1 1 0 0 1-1 1H4a1 1 0 0 1-1-1V1a1 1 0 0 1 1-1zm1 2v10h6V2zm3 11a1 1 0 1 0 0 2 1 1 0 0 0 0-2z"/></svg>
        856-514-7093
      </li>
      <li>
        <svg viewBox="0 0 16 16" aria-hidden="true"><path d="M1 3h14v10H1z M1.5 3.5L8 9l6.5-5.5" stroke="#1d1d1f" stroke-width="1.2"/></svg>
        marcus@brunoly.example
      </li>
      <li>
        <svg viewBox="0 0 16 16" aria-hidden="true"><path d="M8 0a8 8 0 1 0 0 16A8 8 0 0 0 8 0zm0 1.5c.9 1 1.6 2.5 1.9 4H6.1c.3-1.5 1-3 1.9-4zM1.7 7h2.8a12 12 0 0 0 0 2H1.7a6.5 6.5 0 0 1 0-2zm4.3 0h4a10 10 0 0 1 0 2H6a10 10 0 0 1 0-2zm5.5 0h2.8a6.5 6.5 0 0 1 0 2h-2.8a12 12 0 0 0 0-2zM6.1 10.5h3.8c-.3 1.5-1 3-1.9 4-.9-1-1.6-2.5-1.9-4z"/></svg>
        www.brunoly.example
      </li>
    </ul>
  </section>

</body>
</html>
```